Brindle Tides Boat Business Website

I would like a website that looks fresh, fun and exciting with great colors and photos of people having fun sailing and power boating. Current web page is www.brindletides.example. I want to be able to change content and photos myself once completed. Also needs to have customized info request forms and access to enrollment forms. Should work across all browsers and platforms including iPad and Mac. I have three product lines...instruction, charters and trips. See also keelhour.example/new-york, and facebook.com/brindletides, /keelhournewyork and /conchlagoonbar.
Updates

Reason: We are reviewing the designs submitted and will provide feedback asap. Thank you.

Industry/Entity Type

Business

Requirements
Must have
• self management/content management
form submissions
color, fun, excitement
links pages
photo pages
Nice to have
• calendar/class scheduling
guest book
visitor uploadable photos

```html
<!DOCTYPE html>
<html lang="en">
<head>
<meta charset="utf-8">
<title>Brindle Tides Charter Co. and Nautical School</title>
<link rel="stylesheet" href="https://fonts.googleapis.com/css2?family=Open+Sans:ital,wght@0,400;0,600;1,400;1,600&family=Roboto+Condensed:ital,wght@0,400;0,700;1,700&display=swap">
<style>
:root{
  --teal:#22b8a6;
  --sea:#1a8fc9;
  --navy:#0d4f86;
  --navy-dark:#083a66;
  --orange:#f7921e;
  --orange-dark:#e06f0c;
  --gold:#ffd21f;
  --ink:#4a4a4a;
  --muted:#8c8c8c;
  --paper:#f6f6f6;
  --line:#d9d9d9;
  --white:#ffffff;
}
*{box-sizing:border-box;margin:0;padding:0}
html,body{width:797px;height:1200px;overflow:hidden}
body{position:relative;background:var(--paper);font-family:"Open Sans",sans-serif;color:var(--ink)}

.site-header{position:absolute;left:0;top:0;width:797px;height:124px;background:var(--white)}
.brand-name{position:absolute;left:20px;top:44px;font-family:"Open Sans",sans-serif;font-weight:600;font-size:25px;color:var(--navy);line-height:1}
.brand-tag{position:absolute;left:20px;top:76px;font-size:10px;letter-spacing:1px;color:var(--navy);text-transform:uppercase}
.welcome-title{position:absolute;left:270px;top:24px;width:340px;text-align:center;font-family:"Roboto Condensed",sans-serif;font-weight:700;font-size:21px;line-height:28px;color:var(--teal)}
.welcome-title .dark{color:var(--navy)}
.social{position:absolute;right:28px;top:17px;display:flex;gap:6px}
.social span{width:20px;height:20px;border-radius:50%;background:#9a9a9a}
.social span:first-child{background:#3b7fd0}
.quote-btn{position:absolute;left:648px;top:51px;width:132px;height:33px;background:linear-gradient(var(--orange),var(--orange-dark));border-radius:4px;color:var(--white);font-family:"Roboto Condensed",sans-serif;font-weight:700;font-size:14px;display:flex;align-items:center;gap:8px;padding-left:10px}
.quote-btn::after{content:"";position:absolute;left:26px;bottom:-8px;border-left:8px solid transparent;border-top:8px solid var(--orange-dark)}

.main-nav{position:absolute;left:17px;top:102px;width:765px;height:48px;background:linear-gradient(#1d7ec4,var(--navy) 60%,var(--navy-dark));border-radius:4px;display:flex;align-items:center;padding-left:5px;z-index:2;box-shadow:0 3px 4px rgba(0,0,0,.25)}
.main-nav a{font-family:"Roboto Condensed",sans-serif;font-weight:700;font-size:14px;color:var(--white);text-decoration:none;padding:0 15px;line-height:30px;border-right:1px solid rgba(255,255,255,.2)}
.main-nav a:last-child{border-right:none}
.main-nav a.current{color:var(--gold);border:1px solid rgba(255,255,255,.35);border-radius:16px;padding:0 17px;margin-right:6px}

.hero{position:absolute;left:0;top:124px;width:797px;height:420px;background:linear-gradient(#9ec3e2 0%,#cfe0ea 48%,#5f9fa7 52%,#3f8a90 100%)}
.hero-title{position:absolute;left:24px;top:88px;font-family:"Roboto Condensed",sans-serif;font-weight:700;font-size:38px;line-height:48px;color:var(--navy-dark);text-shadow:0 0 3px #fff,0 0 3px #fff}
.hero-title .tint{color:var(--teal)}

.intro{position:absolute;left:20px;top:561px;width:528px;height:166px}
.section-title{font-family:"Roboto Condensed",sans-serif;font-style:italic;font-weight:700;font-size:23px;color:var(--sea);padding-bottom:4px;border-bottom:1px dashed var(--line);width:270px}
.intro p{font-size:9.4px;line-height:17px;margin-top:8px}
.read-more{position:absolute;right:0;top:155px;font-style:italic;font-size:8px;color:var(--sea)}

.login{position:absolute;left:572px;top:566px;width:208px;height:158px;background:#eeeeee;border:2px solid var(--white);box-shadow:0 0 3px rgba(0,0,0,.2)}
.login h3{height:34px;background:linear-gradient(var(--orange),var(--orange-dark));color:var(--white);font-family:"Roboto Condensed",sans-serif;font-style:italic;font-weight:700;font-size:17px;text-align:center;line-height:34px;position:relative}
.login h3::after{content:"";position:absolute;left:96px;bottom:-8px;border-left:9px solid transparent;border-right:9px solid transparent;border-top:8px solid var(--orange-dark)}
.field{display:block;margin:16px 12px 0;height:26px;background:var(--white);border:1px solid var(--line);font-style:italic;font-size:9px;color:var(--muted);line-height:24px;padding-left:8px}
.field+.field{margin-top:8px}
.login-btn{position:absolute;left:66px;bottom:10px;width:76px;height:24px;background:linear-gradient(#1d7ec4,var(--navy-dark));border-radius:12px 12px 0 0;color:var(--white);font-family:"Roboto Condensed",sans-serif;font-weight:700;font-size:11px;text-align:center;line-height:24px;letter-spacing:1px}

.card{position:absolute;top:746px;width:236px;height:206px;background:#efefef;border:3px solid var(--white);box-shadow:0 0 3px rgba(0,0,0,.2)}
.card-instruction{left:20px;background:var(--sea);border-top:8px solid var(--orange)}
.card-instruction h3{font-family:"Roboto Condensed",sans-serif;font-style:italic;font-weight:700;font-size:22px;color:var(--white);margin:14px 0 0 14px}
.card-instruction p{font-style:italic;font-weight:600;font-size:8.5px;line-height:17px;color:var(--white);margin:6px 12px 0 14px}
.card-instruction .notch{position:absolute;left:108px;top:0;border-left:8px solid transparent;border-right:8px solid transparent;border-top:8px solid var(--orange)}
.icon-btn{position:absolute;bottom:0;width:34px;height:28px;display:flex;align-items:center;justify-content:center}
.icon-search{right:36px;background:var(--orange)}
.icon-link{right:0;background:var(--teal)}
.card-charters{left:282px}
.card-trips{left:544px}
.card-photo{height:148px;margin:2px}
.card-charters .card-photo{background:linear-gradient(#c4cfd8,#6d8a9e 45%,#2d5064)}
.card-trips .card-photo{background:linear-gradient(#7fb0d6,#2b73b3 55%,#d9e6ef)}
.card h4{text-align:center;font-family:"Roboto Condensed",sans-serif;font-style:italic;font-weight:700;font-size:22px;color:var(--sea);margin-top:14px}

.footer-brand{position:absolute;left:0;top:1020px;width:797px;text-align:center;font-family:"Open Sans",sans-serif;font-weight:600;font-size:58px;line-height:70px;color:var(--sea)}
.footer-nav{position:absolute;left:0;top:1156px;width:797px;text-align:center;font-size:9.5px;color:var(--muted)}
.footer-nav a{color:var(--muted);text-decoration:none}
.footer-nav a.current{color:var(--orange)}
.footer-nav i{font-style:normal;margin:0 4px;color:#bbb}
.copyright{position:absolute;left:0;top:1176px;width:797px;text-align:center;font-size:9px;color:#a5a5a5}
</style>
</head>
<body>

<header class="site-header">
  <div class="brand-name">Brindle Tides</div>
  <div class="brand-tag">Charter Co. &amp; Nautical School</div>
  <h1 class="welcome-title">Welcome to <span class="dark">Brindle Tides</span><br>Charter Co. and <span class="dark">Nautical</span> School!</h1>
  <div class="social"><span></span><span></span><span></span></div>
  <a class="quote-btn">
    <svg width="18" height="18" viewBox="0 0 18 18" fill="none" stroke="#fff" stroke-width="2"><path d="M8 3H2v13h13v-6"/><path d="M7 11l1-3 7-7 2 2-7 7z"/></svg>
    Request a Quote
  </a>
</header>

<nav class="main-nav">
  <a class="current">Home</a>
  <a>Nautical School</a>
  <a>Charter Sailing</a>
  <a>Charter Power</a>
  <a>Our Captains</a>
  <a>Adventure Travel</a>
  <a>Contact Us</a>
</nav>

<section class="hero" role="img" aria-label="Photo of a white motor yacht cruising on open water with a city skyline behind">
  <h2 class="hero-title">Lorem <span class="tint">ipsum dolor sit amet,</span><br>&nbsp;consectetur <span class="tint">adipiscing elit.</span></h2>
</section>

<section class="intro">
  <h2 class="section-title">Welcome to Brindle Tides</h2>
  <p>Few, if any, locations in Manhattan offer you a wider range of boating options than Brindle Tides Charter Co. and Nautical School. If you're interested in boating on New York's 'Sixth Borough', whether your a sailor or power boater, scallywag or seasoned salt, chances are we've got something you're looking for.</p>
  <p>We operate KeelHour New York (www.keelhour.example/new-york) the world's largest fractional boating company with bases in the US, Europe and Australia offering seasonal memberships on sail and power boats from 25' through 50'. We take the hassle and cost out of boating by providing access to a professionally maintained fleet</p>
  <a class="read-more">Read more...</a>
</section>

<aside class="login">
  <h3>Login enrollment forms</h3>
  <span class="field">Name :</span>
  <span class="field">Email :</span>
  <span class="login-btn">LOGIN</span>
</aside>

<article class="card card-instruction">
  <span class="notch"></span>
  <h3>Instruction</h3>
  <p>Lorem ipsum dolor sit amet, consectetur adipiscing elit. Suspendisse tincidunt interdum sollicitudin. Nullam quis lacus enim. Curabitur nec dolor tellus, non eleifend mauris. Maecenas nec lacus velit. Aliquam at quam lacus,</p>
  <span class="icon-btn icon-search"><svg width="14" height="14" viewBox="0 0 14 14" fill="none" stroke="#fff" stroke-width="2"><circle cx="6" cy="6" r="4"/><path d="M9 9l4 4"/></svg></span>
  <span class="icon-btn icon-link"><svg width="16" height="16" viewBox="0 0 16 16" fill="none" stroke="#fff" stroke-width="2"><rect x="1" y="8" width="8" height="4" rx="2" transform="rotate(-45 5 10)"/><rect x="7" y="4" width="8" height="4" rx="2" transform="rotate(-45 11 6)"/></svg></span>
</article>

<article class="card card-charters">
  <div class="card-photo" role="img" aria-label="Photo of fishing rods on the stern of a boat with a wake and mountains behind"></div>
  <h4>Charters</h4>
</article>

<article class="card card-trips">
  <div class="card-photo" role="img" aria-label="Photo of a couple riding a jet ski across splashing water"></div>
  <h4>Trips</h4>
</article>

<div class="footer-brand">Brindle Tides</div>

<footer>
  <div class="footer-nav">
    <a class="current">Home</a><i>/</i><a>Nautical School</a><i>/</i><a>Charter Sailing</a><i>/</i><a>Charter Power</a><i>/</i><a>Our Captains</a><i>/</i><a>Adventure Travel</a><i>/</i><a>Contact Us</a><i>/</i><a>Sitemap</a>
  </div>
  <div class="copyright">Content copyright 2013. Brindle Tides Charter Co. and Nautical School. All rights reserved.</div>
</footer>

</body>
</html>
```